Ground breaking athletic gear company needs a kick ass business card

We are an American start up athletic gear company that uses a medically proven biohack to boost athletic performance. Heat kills strength and endurance. Our gear helps athletes manage heat better and ultimatley can improve them by up to 10% instantly. Nothing like it out there! Launching this summer.
We are looking for a modern, minimalist design that captures a sporty edge. Check out www.velmarunwear.com, @velmarunwear on instagram for more ideas.

Target Market(s)

25-35 year olds, male and female athletes, vaultlift athletes, competitive runners

Industry/Entity Type

Business

Contact Information for Business Card

Dorian Pellham
Founder
dorianp@velmarunwear.com
www.VelmaRunwear.com
+1 (555) 014-2286

Font styles to use
Sans Serif

Requirements
Must have
• Logo and icon
• All contact information
• dorianp@velmarunwear.com
• +1 (555) 019-4471 M
• +1 (555) 014-2286
Nice to have
• Tag line : "Chill & Charge"

```html
<!DOCTYPE html>
<html lang="en">
<head>
<meta charset="utf-8">
<title>Velma Runwear — Business Card</title>
<link rel="stylesheet" href="https://fonts.googleapis.com/css2?family=Questrial&family=Open+Sans:wght@400&display=swap">
<style>
  :root {
    --backdrop: #5b4b3f;
    --card-white: #ffffff;
    --card-black: #050505;
    --ink-dark: #0a0a0a;
    --ink-light: #ffffff;
    --divider: #b9b9b9;
  }
  * { margin: 0; padding: 0; box-sizing: border-box; }
  html, body {
    width: 1200px;
    height: 987px;
    overflow: hidden;
    background: var(--backdrop);
  }
  .canvas {
    position: relative;
    width: 1200px;
    height: 987px;
  }
  .card {
    position: absolute;
    left: 293px;
    width: 615px;
    height: 350px;
    overflow: hidden;
  }
  .card--front { top: 130px; background: var(--card-white); }
  .card--back { top: 505px; background: var(--card-black); }

  .brand {
    position: absolute;
    left: 0;
    right: 0;
    display: flex;
    align-items: center;
    justify-content: center;
    gap: 12px;
    font-family: "Questrial", sans-serif;
    font-size: 34px;
    line-height: 42px;
    letter-spacing: 0.04em;
  }
  .brand__square {
    width: 18px;
    height: 18px;
  }
  .card--front .brand { top: 100px; color: var(--ink-dark); }
  .card--front .brand__square { background: var(--ink-dark); }
  .card--back .brand { top: 155px; color: var(--ink-light); }
  .card--back .brand__square { background: var(--ink-light); }

  .contact-band {
    position: absolute;
    left: 0;
    top: 239px;
    width: 100%;
    height: 111px;
    background: var(--card-black);
    border-top: 3px solid var(--divider);
    color: var(--ink-light);
    font-family: "Questrial", sans-serif;
    text-align: center;
  }
  .contact-band__name {
    margin-top: 21px;
    font-size: 24px;
    line-height: 30px;
  }
  .contact-band__role { font-size: 19px; }
  .contact-band__details {
    margin-top: 9px;
    font-size: 17px;
    line-height: 22px;
    white-space: nowrap;
  }
  .contact-band__sep { padding: 0 6px; }

  .tagline {
    position: absolute;
    left: 44px;
    right: 58px;
    top: 292px;
    display: flex;
    align-items: center;
    gap: 8px;
    color: var(--ink-light);
    font-family: "Open Sans", sans-serif;
    font-size: 14px;
    line-height: 20px;
    letter-spacing: 0.1em;
    white-space: nowrap;
  }
  .tagline__rule {
    flex: 1;
    height: 1px;
  }
  .tagline__rule--left { background: linear-gradient(to right, rgba(255,255,255,0), #ffffff); }
  .tagline__rule--right { background: linear-gradient(to left, rgba(255,255,255,0), #ffffff); }
</style>
</head>
<body>
<main class="canvas">
  <section class="card card--front" aria-label="Business card front">
    <div class="brand"><span class="brand__square"></span><span class="brand__name">Velma Runwear</span></div>
    <div class="contact-band">
      <p class="contact-band__name">Dorian Pellham - <span class="contact-band__role">Founder</span></p>
      <p class="contact-band__details">+1 (555) 014-2286<span class="contact-band__sep">|</span>dorianp@velmarunwear.com<span class="contact-band__sep">|</span>www.VelmaRunwear.com</p>
    </div>
  </section>

  <section class="card card--back" aria-label="Business card back">
    <div class="brand"><span class="brand__square"></span><span class="brand__name">Velma Runwear</span></div>
    <div class="tagline">
      <span class="tagline__rule tagline__rule--left"></span>
      <span class="tagline__text">CHILL &amp; CHARGE</span>
      <span class="tagline__rule tagline__rule--right"></span>
    </div>
  </section>
</main>
</body>
</html>
```